Tarnwick Electrical Contracting VAN Wrap Design

Hi
I would like a design for my van.
I run an electrical contracting business Tarnwick Electrical Contracting and would like the design to be attention grabbing.
We are based in Gooseberry Hill WA and Esperance WA. We specialise in Residential and Rural although we can complete Commercial works. I pride myself on top class workmanship and being reliable.
I am happy for the whole van to be vinyl wrapped if needed for the design. The Van is a LWB Med Roof Velmor Haulex 2016. I would like to it to be a moving advertisement board.
It should include
My logo
My Contact number 0471 926 534
My Electrical Contractors (EC) number 27364
Established 2015
Space for future website

I'm not a big fan of the traditional spark, power point etc for electrical company and would like something different

Target Market(s)

Anyone on the road that sees the van !!

Industry/Entity Type

Electrical contracting : Residential and Rural Electrical Installations

Colors
0054AA
0677BA
7BADD7
CADEEF
E8F1F8
59FF00
82FF00
B8FF75
E3FFCB
F4FFEA
FFC000
F8CF3A
FAE287
FDF2CF
FEFAEE
F0912C
F2A743
F7CA91
FBE8D2
FDF5EE
EB3D1F
EC4F4E
F09395
F8D3D4
FCEDEE

Requirements
Must have
• TEL 0471 926 534 - EC 27364 - My logo - Services offered Residential and Rural throughout the Hills, "Tarnwick Electrical: Bright Homes, Happy Families"
Nice to have
• any catchy slogans, enjoyable to see, makes peopele talk
Should not have
• Traditional electrical sparks power points etc

```html
<!DOCTYPE html>
<html lang="en">
<head>
<meta charset="utf-8">
<title>Tarnwick Electrical Contracting – Van Wrap Sides</title>
<link rel="stylesheet" href="https://fonts.googleapis.com/css2?family=Arimo:wght@400&family=Pinyon+Script&display=swap">
<style>
  :root {
    --navy: #0b2257;
    --blue-top: #2f7cc0;
    --blue-mid: #5aa6dc;
    --blue-low: #a7ddf6;
    --edge-blue: #3a8ad6;
    --accent-blue: #0054aa;
    --page: #ffffff;
  }
  html, body {
    margin: 0;
    padding: 0;
    width: 1172px;
    height: 1200px;
    overflow: hidden;
    background: var(--page);
  }
  .wrap-sides {
    display: block;
    width: 1172px;
    height: 1200px;
  }
  .contact-name { font: 400 22px "Arimo", Arial, sans-serif; fill: var(--navy); }
  .contact-phone { font: 400 37px "Arimo", Arial, sans-serif; fill: var(--navy); letter-spacing: 0.5px; }
  .brand-name { font: 400 34px "Arimo", Arial, sans-serif; fill: var(--navy); }
  .brand-line { font: 400 20px "Arimo", Arial, sans-serif; fill: var(--navy); }
  .tagline { font: 400 28px "Pinyon Script", cursive; fill: var(--navy); }
  .contact-email { font: 400 15px "Arimo", Arial, sans-serif; fill: var(--navy); }
  .slogan { font: 400 17px "Arimo", Arial, sans-serif; fill: var(--accent-blue); }
  .service-line { font: 400 15px "Arimo", Arial, sans-serif; fill: var(--navy); }
  .licence-line { font: 400 15px "Arimo", Arial, sans-serif; fill: var(--navy); letter-spacing: 0.5px; }
  .brand-square { fill: var(--navy); }
  .icon { fill: none; stroke: var(--navy); stroke-width: 2; }
  .icon-solid { fill: var(--navy); }
  .band-edge { fill: none; stroke: var(--edge-blue); stroke-width: 6; }
</style>
</head>
<body>
<svg class="wrap-sides" viewBox="0 0 1172 1200" xmlns="http://www.w3.org/2000/svg" role="img" aria-label="Tarnwick Electrical Contracting van wrap, driver and passenger sides">
  <defs>
    <linearGradient id="bandGradient" x1="0" y1="0" x2="0" y2="1">
      <stop offset="0" stop-color="var(--blue-top)"/>
      <stop offset="0.5" stop-color="var(--blue-mid)"/>
      <stop offset="1" stop-color="var(--blue-low)"/>
    </linearGradient>
    <symbol id="phoneIcon" viewBox="0 0 40 40">
      <path class="icon-solid" d="M9 4c2-1 4 0 5 2l3 6c1 2 0 3-1 4l-2 2c1 4 5 8 9 10l2-2c1-1 3-2 4-1l6 3c2 1 3 3 2 5l-2 3c-2 2-5 3-8 2C16 35 5 24 3 13c-1-3 0-6 2-8z"/>
      <path class="icon" stroke-width="3" d="M23 6a12 12 0 0 1 11 11M22 12a6 6 0 0 1 6 6"/>
    </symbol>
    <symbol id="globeIcon" viewBox="0 0 28 28">
      <circle class="icon" cx="14" cy="14" r="12"/>
      <ellipse class="icon" cx="14" cy="14" rx="5" ry="12"/>
      <path class="icon" d="M2 14h24M4 8h20M4 20h20"/>
    </symbol>
  </defs>

  <!-- Driver side -->
  <g class="side side-left">
    <path class="colour-band" fill="url(#bandGradient)" d="M62 62 Q62 52 72 52 L402 52 Q428 100 428 210 Q428 300 425 372 L62 372 Z"/>
    <path class="band-edge" d="M402 52 Q428 100 428 210 Q428 300 425 372"/>
    <rect class="brand-square" x="100" y="62" width="134" height="188" rx="4"/>
    <text class="brand-name" x="254" y="176">Tarnwick</text>
    <text class="brand-line" x="254" y="202">Electrical Contracting</text>
    <text class="tagline" x="278" y="232">A reputation for reliability</text>

    <text class="contact-name" x="434" y="100">Dorian Welkes</text>
    <use href="#phoneIcon" x="412" y="114" width="38" height="38"/>
    <text class="contact-phone" x="462" y="146">0471 926 534</text>

    <text class="slogan" x="452" y="284">Tarnwick Electrical: Bright Homes, Happy Families</text>
    <text class="service-line" x="452" y="310">Residential &amp; Rural throughout the Hills</text>
    <text class="licence-line" x="452" y="336">EC 27364 · Established 2015</text>

    <use href="#globeIcon" x="89" y="294" width="25" height="25"/>
    <text class="contact-email" x="122" y="312">dorian@tarnwickelectrical.com.au</text>
  </g>

  <!-- Passenger side -->
  <g class="side side-right">
    <path class="colour-band" fill="url(#bandGradient)" d="M1104 657 L770 657 Q745 710 745 810 Q745 900 748 977 L1114 977 L1114 667 Q1114 657 1104 657 Z"/>
    <path class="band-edge" d="M770 657 Q745 710 745 810 Q745 900 748 977"/>
    <rect class="brand-square" x="939" y="668" width="132" height="188" rx="4"/>
    <text class="brand-name" x="919" y="782" text-anchor="end">Tarnwick</text>
    <text class="brand-line" x="917" y="806" text-anchor="end">Electrical Contracting</text>
    <text class="tagline" x="893" y="837" text-anchor="end">A reputation for reliability</text>

    <text class="contact-name" x="737" y="705" text-anchor="end">Dorian Welkes</text>
    <use href="#phoneIcon" x="490" y="718" width="38" height="38"/>
    <text class="contact-phone" x="539" y="750">0471 926 534</text>

    <text class="slogan" x="728" y="892" text-anchor="end">Tarnwick Electrical: Bright Homes, Happy Families</text>
    <text class="service-line" x="728" y="918" text-anchor="end">Residential &amp; Rural throughout the Hills</text>
    <text class="licence-line" x="728" y="944" text-anchor="end">EC 27364 · Established 2015</text>

    <use href="#globeIcon" x="829" y="901" width="25" height="25"/>
    <text class="contact-email" x="860" y="919" style="font-size:14px">dorian@tarnwickelectrical.com.au</text>
  </g>
</svg>
</body>
</html>
```